Willowmere Loft B&B Business Card

This beautiful high-class B&B is looking for a business card that stands out from the rest. They are in the middle of the countryside, have chickens, geese and a dog. They also love bumble bees.

I was maybe thinking a rustic drawing / print of a bumble bee and a sketch of the house, I am not sure.. I quite like the feel of this... http://www.tarnwick-mill.co.uk/

Industry/Entity Type

Business

Contact Information for Business Card

Willowmere Loft
Bed & Breakfast
Brackleford, Hensworth, Somerset, TA14 7QP
01632 960418 | www.willowmereloft.co.uk

```html
<!DOCTYPE html>
<html lang="en">
<head>
<meta charset="utf-8">
<title>Willowmere Loft B&amp;B – Business Card</title>
<link rel="stylesheet" href="https://fonts.googleapis.com/css2?family=Roboto+Condensed:wght@400;700&display=swap">
<style>
  :root {
    --cream: #fbf8ea;
    --orange: #f47a17;
    --ink: #111111;
    --white: #ffffff;
    --sky: #5f8fd0;
    --cloud: #e8ecef;
    --stone: #e6dfc9;
    --roof: #c9574a;
    --lawn: #3f7a2c;
    --gravel: #d9cfb8;
  }
  * { margin: 0; padding: 0; box-sizing: border-box; }
  html, body { width: 1200px; height: 688px; overflow: hidden; background: var(--cream); }
  .card {
    position: relative;
    width: 1200px;
    height: 688px;
    background: var(--cream);
    font-family: "Roboto Condensed", "Arial Narrow", sans-serif;
    overflow: hidden;
  }
  .house-photo { position: absolute; left: 0; top: 0; width: 690px; height: 688px; }
  .brand {
    position: absolute;
    left: 740px;
    top: 150px;
    padding-left: 12px;
    border-left: 4px solid var(--ink);
  }
  .brand-name {
    color: var(--orange);
    font-weight: 700;
    font-size: 37px;
    line-height: 42px;
    letter-spacing: 0.3px;
  }
  .brand-tagline {
    color: var(--ink);
    font-size: 27px;
    line-height: 36px;
  }
  .address {
    position: absolute;
    left: 738px;
    top: 240px;
    color: var(--ink);
    font-size: 26px;
    line-height: 40px;
  }
  .contact-list { list-style: none; }
  .contact-item {
    position: absolute;
    left: 743px;
    width: 470px;
    height: 63px;
    background: var(--ink);
    border-radius: 32px 0 0 32px;
    display: flex;
    align-items: center;
    color: var(--orange);
    font-size: 25px;
  }
  .contact-item.phone { top: 353px; }
  .contact-item.web { top: 433px; }
  .contact-item.social { top: 515px; }
  .contact-icon {
    width: 44px;
    height: 44px;
    margin: 0 22px 0 10px;
    border-radius: 50%;
    background: var(--orange);
    display: flex;
    align-items: center;
    justify-content: center;
    flex: none;
  }
  .contact-icon svg { width: 20px; height: 20px; }
</style>
</head>
<body>
<main class="card">
  <svg class="house-photo" viewBox="0 0 690 688" role="img" aria-label="Photograph of the stone barn guesthouse with red tiled roof, gravel drive and lawn under a cloudy blue sky">
    <defs>
      <linearGradient id="photo-tones" x1="0" y1="0" x2="0" y2="1">
        <stop offset="0" stop-color="var(--sky)"/>
        <stop offset="0.2" stop-color="var(--cloud)"/>
        <stop offset="0.3" stop-color="var(--roof)"/>
        <stop offset="0.38" stop-color="var(--stone)"/>
        <stop offset="0.58" stop-color="var(--stone)"/>
        <stop offset="0.66" stop-color="var(--lawn)"/>
        <stop offset="0.72" stop-color="var(--gravel)"/>
        <stop offset="0.86" stop-color="var(--gravel)"/>
        <stop offset="1" stop-color="var(--lawn)"/>
      </linearGradient>
      <pattern id="scallop-edge" x="0" y="-4" width="20" height="34" patternUnits="userSpaceOnUse">
        <circle cx="0" cy="17" r="11" fill="black"/>
      </pattern>
      <mask id="stamp-edge">
        <rect width="690" height="688" fill="white"/>
        <rect x="672" y="0" width="18" height="688" fill="black"/>
        <rect x="661" y="0" width="20" height="688" fill="url(#scallop-edge)" transform="translate(20 0)"/>
      </mask>
      <pattern id="left-scallops" x="0" y="2" width="20" height="34" patternUnits="userSpaceOnUse">
        <circle cx="0" cy="17" r="10" fill="var(--orange)"/>
      </pattern>
    </defs>
    <rect width="690" height="688" fill="url(#photo-tones)" mask="url(#stamp-edge)"/>
    <rect x="0" y="0" width="12" height="688" fill="url(#left-scallops)"/>
  </svg>

  <header class="brand">
    <h1 class="brand-name">WILLOWMERE LOFT</h1>
    <p class="brand-tagline">Bed &amp; Breakfast</p>
  </header>

  <address class="address">Brackleford, Hensworth, Somerset,<br>TA14 7QP</address>

  <ul class="contact-list">
    <li class="contact-item phone">
      <span class="contact-icon">
        <svg viewBox="0 0 24 24" aria-hidden="true"><path fill="var(--white)" d="M6.6 10.8c1.4 2.8 3.8 5.1 6.6 6.6l2.2-2.2c.3-.3.7-.4 1-.2 1.1.4 2.3.6 3.6.6.6 0 1 .4 1 1V20c0 .6-.4 1-1 1C10.6 21 3 13.4 3 4c0-.6.4-1 1-1h3.5c.6 0 1 .4 1 1 0 1.2.2 2.4.6 3.6.1.3 0 .7-.2 1z"/></svg>
      </span>
      01632 960418
    </li>
    <li class="contact-item web">
      <span class="contact-icon">
        <svg viewBox="0 0 24 24" aria-hidden="true"><circle cx="12" cy="12" r="9" fill="none" stroke="var(--white)" stroke-width="2.4"/><ellipse cx="12" cy="12" rx="4" ry="9" fill="none" stroke="var(--white)" stroke-width="2"/><line x1="3" y1="12" x2="21" y2="12" stroke="var(--white)" stroke-width="2"/></svg>
      </span>
      www.willowmereloft.co.uk
    </li>
    <li class="contact-item social">
      <span class="contact-icon"></span>
      Willowmere Loft Bed and Breakfast
    </li>
  </ul>
</main>
</body>
</html>
```